Trade show flier

Need a two sided flier for a trade show that will go with the trade show banner you are designing for us. We have included some information we would like to see o the flier. We do need to work on the content. If you can start a design, we can work on the content. This must be done by 3/12/2018

Manufacturing companies

Trade

```html
<!DOCTYPE html>
<html lang="en">
<head>
<meta charset="utf-8">
<title>Relay Works – Trade Show Flier</title>
<link href="https://fonts.googleapis.com/css2?family=Lato:wght@400;700&family=Open+Sans:wght@400;600;700&display=swap" rel="stylesheet">
<style>
  :root{
    --bg:#3a3b3d;
    --blue:#1f74c6;
    --blue-dark:#15579b;
    --ink:#2c2c2c;
    --paper:#ffffff;
    --rule:#9a9ca0;
  }
  *{box-sizing:border-box;margin:0;padding:0}
  html,body{width:1200px;height:776px;overflow:hidden;background:var(--bg)}
  body{position:relative;font-family:"Open Sans",Arial,sans-serif;color:var(--ink)}
  .page{position:absolute;top:38px;width:495px;height:700px;background:var(--paper);overflow:hidden;box-shadow:0 10px 24px rgba(0,0,0,.45)}
  .page--front{left:70px}
  .page--back{left:635px}
  .edge{position:absolute;left:0;right:0;background:var(--blue)}
  .edge--top{top:0;height:7px}
  .edge--bottom{bottom:0;height:12px}

  /* front */
  .masthead{position:absolute;top:7px;left:0;right:0;height:108px;background:linear-gradient(#fff,#f1f2f4)}
  .masthead__shape{position:absolute;right:0;top:20px}
  .brand{position:absolute;left:34px;top:36px;display:flex;align-items:center;gap:10px}
  .brand__dot{width:40px;height:40px;border-radius:50%;background:var(--blue)}
  .brand__name{font-family:"Lato",sans-serif;font-weight:700;font-size:31px;color:var(--blue);letter-spacing:1px;line-height:1}
  .hero{position:absolute;top:115px;left:0;right:0;height:240px;background:linear-gradient(100deg,#1b3f78 0%,#2f6db3 45%,#6b93c6 70%,#274d86 100%)}
  .profile{position:absolute;top:372px;left:30px;width:272px}
  .heading{display:flex;align-items:center;gap:8px;font-size:17px;font-weight:600;color:var(--blue);margin-bottom:6px}
  .heading::before{content:"";width:0;height:0;border-left:9px solid transparent;border-bottom:9px solid #222}
  .copy{font-size:9.5px;line-height:1.45;color:#222;margin-bottom:14px}
  .side-photo{position:absolute;top:380px;right:30px;width:138px;height:272px;border:2px solid #123;background:linear-gradient(160deg,#0a1f5c,#2a56c4 55%,#0b1a4a)}

  /* back */
  .services{position:absolute;top:20px;left:26px;right:22px}
  .services__title{font-size:14px;font-weight:600;color:var(--blue-dark);display:flex;align-items:center;gap:7px;margin-bottom:7px}
  .services__title::before{content:"";border-left:8px solid transparent;border-bottom:8px solid #222}
  .services__cols{display:grid;grid-template-columns:1fr 1fr;column-gap:24px}
  .svc{margin-bottom:6px}
  .svc__name{font-size:9px;font-weight:700;color:var(--blue);line-height:1.3}
  .svc__desc{font-size:8px;line-height:1.2;color:#333}
  .divider{position:absolute;left:0;right:0;height:6px;background:var(--rule)}
  .support{position:absolute;top:242px;left:0;right:0;height:230px;background:linear-gradient(#e9eaec,#f7f7f8)}
  .support__title{position:absolute;top:12px;left:30px;font-size:12px;font-weight:600;color:var(--blue-dark);display:flex;align-items:center;gap:7px}
  .support__title::before{content:"";border-left:8px solid transparent;border-bottom:8px solid #222}
  .support__list{position:absolute;top:34px;left:46px;width:260px;font-size:8px;line-height:11.6px;color:#222}
  .support__list li{margin-left:10px}
  .support__list li::marker{color:var(--blue)}
  .servers{position:absolute;top:34px;right:26px;width:160px;height:160px;background:radial-gradient(ellipse at 50% 45%,#cfd3d8 0%,#9fa6ae 45%,#eef0f2 80%)}
  .partners{position:absolute;top:478px;left:0;right:0;bottom:12px;padding:18px 26px 0}
  .partners__line{font-size:9px;font-weight:700;color:var(--blue);text-align:center;line-height:1.35;font-style:italic}
  .partners__grid{display:grid;grid-template-columns:repeat(4,1fr);gap:18px 16px;margin-top:22px}
  .badge{height:38px;border-radius:4px;background:#d7dadf}
  .badge--blue{background:#bcd3ec}
  .badge--orange{background:#f3d2b9}
  .badge--red{background:#f0c3c3}
  .badge--green{background:#c6e3cf}
</style>
</head>
<body>

<section class="page page--front">
  <div class="edge edge--top"></div>
  <header class="masthead">
    <div class="brand">
      <span class="brand__dot"></span>
      <span class="brand__name">Relay Works</span>
    </div>
    <svg class="masthead__shape" width="180" height="88" viewBox="0 0 180 88" aria-hidden="true">
      <polygon points="30,0 180,0 180,88 0,88" fill="#1f74c6"/>
    </svg>
  </header>
  <div class="hero" role="img" aria-label="Technician with a tablet working at a server rack, tinted blue"></div>

  <div class="profile">
    <h2 class="heading">Company Profile:</h2>
    <p class="copy">Established in 2006, Relay Works is a Managed IT Service firm providing exceptional IT consultation and support for businesses in the California with 20 – 1000 employees. Our personable, reliable and professional team empowers our clients to make their IT infrastructure a strategic asset.</p>
    <h2 class="heading">Our Vision:</h2>
    <p class="copy">To provide a customer experience that provides value and enables technology collaboration effortlessly.</p>
    <h2 class="heading">Our Mission:</h2>
    <p class="copy">Innovative collaboration to improve business process by leveraging technology that empowers organizations to implement a roadmap to success.</p>
  </div>
  <div class="side-photo" role="img" aria-label="Data centre aisle lit in blue"></div>
  <div class="edge edge--bottom"></div>
</section>

<section class="page page--back">
  <div class="edge edge--top"></div>
  <div class="services">
    <h2 class="services__title">SERVICES:</h2>
    <div class="services__cols">
      <div>
        <div class="svc"><div class="svc__name">Managed Services</div><div class="svc__desc">Proactive support, remediation and maintenance of your technology infrastructure, 24/7.</div></div>
        <div class="svc"><div class="svc__name">Backup and Business Continuity</div><div class="svc__desc">Secure your data while minimizing downtime.</div></div>
        <div class="svc"><div class="svc__name">Virtualization</div><div class="svc__desc">Increase IT flexibility and scalability while minimizing hardware resources.</div></div>
        <div class="svc"><div class="svc__name">Voice Collaboration</div><div class="svc__desc">Voice-over-IP (VOIP) Design and Deployment.</div></div>
        <div class="svc"><div class="svc__name">Cloud Services</div><div class="svc__desc">Leverage cloud support services for remote access and or business continuity.</div></div>
      </div>
      <div>
        <div class="svc"><div class="svc__name">Security Services</div><div class="svc__desc">Multi-faceted approach to addressing your network security.</div></div>
        <div class="svc"><div class="svc__name">Wireless Services</div><div class="svc__desc">Secure connectivity and centralized management for wireless endpoint devices.</div></div>
        <div class="svc"><div class="svc__name">Procurement Services</div><div class="svc__desc">Procurement of industry standard business class product.</div></div>
        <div class="svc"><div class="svc__name">Project Collaboration</div><div class="svc__desc">Strategic technology roadmaps that address company business goals.</div></div>
        <div class="svc"><div class="svc__name">Surveillance Services</div><div class="svc__desc">Intelligent network security video solutions.</div></div>
      </div>
    </div>
  </div>
  <div class="divider" style="top:236px"></div>

  <div class="support">
    <h2 class="support__title">Our BaseLine Managed Services Support include:</h2>
    <ul class="support__list">
      <li>Team of industry certified Network Engineers</li>
      <li>Remote support (Weekdays 7am – 6pm)</li>
      <li>Onsite support (Weekdays 7am – 6pm)</li>
      <li>24x7 network monitoring and remediation</li>
      <li>Daily proactive maintenance</li>
      <li>Managed antivirus software</li>
      <li>Managed ransomware protection</li>
      <li>Ticketing portal to track open tickets and resolutions</li>
      <li>Vendor management</li>
      <li>Network Documentation Management</li>
      <li>Software License Management</li>
      <li>Technology procurement</li>
      <li>Monitoring of existing backup systems and data recovery</li>
      <li>Business continuity planning</li>
      <li>Network and data security planning and testing</li>
      <li>Quarterly IT meetings</li>
    </ul>
    <div class="servers" role="img" aria-label="Three silver server towers with blue lights"></div>
  </div>
  <div class="divider" style="top:472px"></div>

  <div class="partners">
    <p class="partners__line">We provide a great customer service experience with a simplified, cost-effective approach to IT that leverages certified technical professionals with industry standard skills and knowledge.</p>
    <div class="partners__grid">
      <div class="badge"></div>
      <div class="badge badge--orange"></div>
      <div class="badge"></div>
      <div class="badge badge--blue"></div>
      <div class="badge badge--red"></div>
      <div class="badge badge--green"></div>
      <div class="badge"></div>
      <div class="badge badge--orange"></div>
    </div>
  </div>
  <div class="edge edge--bottom"></div>
</section>

</body>
</html>
```